Stationery Design For Specialist London law firm

We have merged two firms of London lawyers to create a new firm with a new name.

The new firms name is KR Holloway. We would like to include the description Solicitors and Advocates in the design.

We need a new design for our headed paper, business cards compliment slips etc.

The image we wish to project is fresh but not gimmicky - reliable and strong but not stuffy.

We have no strong views on font or colour this really is pretty much a blank page.

Our preference is for the name to be at the top of the page

Target Market(s)

Our clients who are individuals rather than corporate and other lawyers

Industry/Entity Type

Law Firm

Requirements
Should not have
• Legal images eg scales of justice etc

Obviously nothing childish or gimmicky

```html
<!DOCTYPE html>
<html lang="en">
<head>
<meta charset="utf-8">
<title>KR Holloway – Stationery</title>
<link rel="stylesheet" href="https://fonts.googleapis.com/css2?family=Barlow:wght@400;700&family=Tinos&display=swap">
<style>
  :root {
    --paper: #ffffff;
    --ink: #1d1d1b;
    --brand-red: #d2313b;
    --brand-yellow: #f6d92b;
    --brand-orange: #e0941e;
    --contact-orange: #eda431;
    --card-text: #f7e27a;
    --card-name: #fff4b8;
    --sans: "Barlow", Arial, sans-serif;
    --serif: "Tinos", "Times New Roman", serif;
  }
  * { margin: 0; padding: 0; box-sizing: border-box; }
  html, body { width: 1200px; height: 900px; overflow: hidden; background: var(--paper); }
  .canvas { position: relative; width: 1200px; height: 900px; overflow: hidden; background: var(--paper); }

  /* Letterhead */
  .letter-contact {
    position: absolute; left: 78px; top: 72px;
    font-family: var(--sans); font-size: 23px; line-height: 26px;
    color: var(--contact-orange); list-style: none;
  }
  .letter-contact .phone { color: var(--brand-red); }

  .letter-brand {
    position: absolute; right: 92px; top: 66px; text-align: right;
    font-family: var(--sans);
  }
  .brand-row { display: flex; align-items: center; justify-content: flex-end; gap: 18px; }
  .brand-square { width: 46px; height: 46px; background: var(--brand-yellow); }
  .brand-name { font-size: 64px; font-weight: 700; color: var(--brand-red); line-height: 1; }
  .brand-tagline {
    margin-top: 10px; font-size: 26px; font-weight: 400; letter-spacing: 1px;
    color: var(--contact-orange); text-transform: uppercase;
  }

  .letter-body {
    position: absolute; left: 48px; top: 350px; width: 660px;
    font-family: var(--serif); font-size: 27px; line-height: 38px; color: var(--ink);
  }
  .letter-date { margin-bottom: 16px; }
  .letter-ref { margin-bottom: 24px; }
  .recipient { font-style: normal; margin-bottom: 68px; }
  .salutation { margin-bottom: 24px; }

  /* Business card */
  .business-card {
    position: absolute; left: 590px; top: 566px; width: 554px; height: 360px;
    background: var(--brand-orange);
    box-shadow: -2px 2px 6px rgba(0,0,0,0.25);
    font-family: var(--sans);
  }
  .card-brand {
    position: absolute; right: 44px; top: 44px; text-align: right;
  }
  .card-brand .brand-square { width: 26px; height: 26px; }
  .card-brand .brand-row { gap: 10px; }
  .card-brand .brand-name { font-size: 40px; }
  .card-brand .brand-tagline { font-size: 15px; margin-top: 6px; color: var(--card-text); }

  .card-contact {
    position: absolute; left: 94px; top: 152px; list-style: none;
    font-size: 18px; line-height: 22px; color: var(--card-text);
  }
  .card-person {
    position: absolute; left: 316px; top: 152px;
    font-size: 18px; line-height: 22px; color: var(--card-text);
  }
  .card-person .person-name { font-weight: 700; color: var(--card-name); }
</style>
</head>
<body>
<div class="canvas">

  <ul class="letter-contact">
    <li>42 Marlowe Row</li>
    <li>London E1 4QP</li>
    <li class="phone">T 020 7946 0312</li>
    <li>M 07700 900 418</li>
    <li>E info@krholloway.co.uk</li>
    <li>W www.krholloway.co.uk</li>
  </ul>

  <header class="letter-brand">
    <div class="brand-row">
      <span class="brand-square"></span>
      <span class="brand-name">KR Holloway</span>
    </div>
    <p class="brand-tagline">Solicitors &amp; Advocates</p>
  </header>

  <main class="letter-body">
    <p class="letter-date">24 November 2012</p>
    <p class="letter-ref">Your Ref: House move</p>
    <address class="recipient">
      M A Pendry<br>
      Larchfield House<br>
      Oakmere Street<br>
      Thornbury<br>
      Kent TN4 2PX
    </address>
    <p class="salutation">Dear Sir, madam</p>
    <p class="letter-text">Veritatis et quasi architecto beatae vitae dicta sunt explicabo. Nemo enim ipsam voluptatem quia voluptas sit aspernatur aut odit aut fugit, sed quia consequuntur magni dolores eos qui ratione voluptatem.</p>
  </main>

  <section class="business-card">
    <div class="card-brand">
      <div class="brand-row">
        <span class="brand-square"></span>
        <span class="brand-name">KR Holloway</span>
      </div>
      <p class="brand-tagline">Solicitors &amp; Advocates</p>
    </div>
    <ul class="card-contact">
      <li>42 Marlowe Row</li>
      <li>London E1 4QP</li>
      <li>T: 020 7946 0312</li>
      <li>M: 07700 900 418</li>
      <li>E: info@krholloway.co.uk</li>
      <li>W: www.krholloway.co.uk</li>
    </ul>
    <div class="card-person">
      <p class="person-name">Daniel Ashford</p>
      <p class="person-role">Partner</p>
      <p class="person-phone">M: 07700 900 527</p>
    </div>
  </section>

</div>
</body>
</html>
```